Website design for Halvard Remit

We need a website design based upon the Halvard Remit look-and-feel. Halvard Remit is all about connecting in the dynamic and fast moving world of (internet and mobile) payments. Our logo and colors (dark blue, grey and white) reflect this. The font we use is " Museo". See attached files. Our website needs to be responsive to the screen of the device used. Preferably based upon the wordpress theme, which supports many widgets and is open source:
http://layoutbazaar.example/item/sole-adaptive-layered-site-template/8163049. Please share your thoughts, suggestions and proposal and let me know what you need me to do or share with you to make this happen. Thanks. Maarten.

Industry/Entity Type

Internet

```html
<!DOCTYPE html>
<html lang="en">
<head>
<meta charset="utf-8">
<title>Halvard Remit</title>
<link href="https://fonts.googleapis.com/css2?family=Roboto:wght@300;400;500;700&display=swap" rel="stylesheet">
<style>
:root{
  --navy:#0b3370;
  --navy-deep:#082a5e;
  --navy-field:#1a4a8a;
  --ink:#333;
  --muted:#8a8a8a;
  --soft:#f0f0f0;
  --line:#d4d4d4;
  --white:#fff;
  --link:#1f5aa6;
}
*{box-sizing:border-box;margin:0;padding:0}
html,body{width:1200px;height:3005px;overflow:hidden}
body{font-family:"Roboto",Arial,sans-serif;color:var(--ink);background:var(--white);position:relative}
.abs{position:absolute}

/* header */
.site-header{left:0;top:0;width:1200px;height:140px;background:var(--navy)}
.brand{left:80px;top:34px;display:flex;align-items:center;gap:14px}
.brand-mark{width:30px;height:30px;border:2px solid var(--white)}
.brand-name{color:var(--white);font-size:22px;font-weight:400}
.account{right:82px;top:24px;color:#9fb4d6;font-size:11px;letter-spacing:.5px}
.account span{margin:0 8px}
.search{left:830px;top:66px;width:290px;height:36px;background:var(--navy-field);border-radius:4px;color:#9fb4d6;font-size:13px;padding:10px 12px}
.search svg{position:absolute;right:10px;top:9px}

/* nav */
.main-nav{left:0;top:140px;width:1200px;height:54px;background:linear-gradient(#f4f4f4,#dedede);border-bottom:1px solid #cfcfcf}
.main-nav ul{list-style:none;display:flex;position:absolute;left:80px;top:0;height:54px}
.main-nav li{font-size:13px;text-transform:uppercase;color:#333;padding:0 21px;line-height:54px;border-right:1px solid #cdcdcd}
.main-nav li:last-child{border-right:0}
.main-nav li.active{background:var(--navy);color:var(--white);padding:0 25px}

/* hero */
.hero{left:0;top:194px;width:1200px;height:468px;background:radial-gradient(ellipse at 60% 40%,#fafafa,#e2e2e2)}
.hero-kicker{left:80px;top:160px;font-size:23px;color:#7a7a7a;text-transform:uppercase}
.hero-title{left:80px;top:190px;font-size:37px;font-weight:700;color:var(--navy)}
.hero-text{left:80px;top:238px;width:470px;font-size:13px;line-height:21px;color:#555}
.hero-dots{left:80px;top:382px;display:flex;gap:8px}
.hero-dots i{width:12px;height:12px;border-radius:50%;border:1.5px solid #777;display:block}
.hero-dots i.on{background:var(--navy);border-color:var(--navy)}
.hero-art{left:610px;top:20px;width:400px;height:420px;border-radius:12px;background:radial-gradient(circle at 55% 25%,#3aa0d8 0 22%,transparent 23%),linear-gradient(#e8eef3,#cfd7dd)}

/* sections */
.section-title{width:1200px;text-align:center;font-size:37px;font-weight:300;color:#333}
.solutions{left:0;top:662px;width:1200px;height:528px;background:var(--white)}
.solution{width:300px;text-align:center}
.solution .badge{width:138px;height:138px;border-radius:50%;background:var(--navy);margin:0 auto;display:flex;align-items:center;justify-content:center}
.solution h3{margin-top:30px;font-size:25px;font-weight:400;color:var(--navy)}
.solution p{margin:10px auto 0;width:262px;font-size:15px;line-height:21px;color:#a5a5a5;font-weight:300}
.btn-outline{display:inline-block;margin-top:30px;width:124px;height:46px;border:1px solid #9aa9bf;border-radius:2px;font-size:13px;line-height:44px;color:var(--navy);text-transform:uppercase}

.about{left:0;top:1190px;width:1200px;height:394px;background:var(--soft)}
.body-copy{left:130px;width:940px;text-align:center;font-size:15px;line-height:31px;color:#666;font-weight:300}
.btn-solid{left:522px;top:310px;width:158px;height:46px;background:var(--navy);color:var(--white);font-size:13px;line-height:46px;text-align:center;text-transform:uppercase;border-radius:2px}

.why{left:0;top:1584px;width:1200px;height:658px;background:var(--white)}
.video{left:222px;top:224px;width:756px;height:370px;background:linear-gradient(135deg,#3b3f44,#1e2124 60%,#2b2e31)}
.video svg{position:absolute;left:328px;top:142px}

.testimonials{left:0;top:2242px;width:1200px;height:544px;background:#efefef}
.avatar{width:132px;height:132px;border-radius:50%;border:4px solid var(--white);background:linear-gradient(#cfd4da,#8e959e);box-shadow:0 1px 4px rgba(0,0,0,.2)}
.quote{width:252px;font-size:13px;line-height:21px;color:#666;font-weight:300}
.quote b{display:block;margin-top:18px;font-weight:400;color:var(--link)}

.site-footer{left:0;top:2786px;width:1200px;height:219px;background:var(--navy)}
.footer-links{left:0;top:44px;width:1200px;display:flex;justify-content:center;gap:41px;font-size:13px;color:#d7e0ee}
.copyright{left:0;top:82px;width:1200px;text-align:center;font-size:13px;color:#d7e0ee}
.social{left:502px;top:140px;display:flex;gap:12px}
.social i{width:40px;height:40px;border-radius:50%;background:#2d63b0;display:block}
</style>
</head>
<body>

<header class="site-header abs">
  <div class="brand abs"><span class="brand-mark"></span><span class="brand-name">Halvard Remit</span></div>
  <div class="account abs">LOGIN<span>|</span>REGISTER</div>
  <div class="search abs">Search
    <svg width="18" height="18" viewBox="0 0 18 18"><circle cx="7.5" cy="7.5" r="5.5" fill="none" stroke="#fff" stroke-width="2.2"/><line x1="11.5" y1="11.5" x2="16" y2="16" stroke="#fff" stroke-width="2.6" stroke-linecap="round"/></svg>
  </div>
</header>

<nav class="main-nav abs">
  <ul>
    <li class="active">Home</li><li>About Us</li><li>Why Halvard Remit</li><li>Services</li><li>Blog</li><li>Testimonials</li><li>Our Partners</li><li>Contact</li>
  </ul>
</nav>

<section class="hero abs">
  <div class="hero-kicker abs">Simple Halvard Remit</div>
  <h1 class="hero-title abs">SAMPLE TEXT HERE</h1>
  <p class="hero-text abs">Anean vulputate eleifend tellus. Aenean leo ligula, porttitor eu, consequat vitae, eleifend ac, enim. Aliquam lorem ante, dapibus in, viverra quis, feugiat a, tellus. Phasellus viverra nulla ut metus varius laoreet.</p>
  <div class="hero-dots abs"><i class="on"></i><i></i><i></i><i></i></div>
  <div class="hero-art abs" role="img" aria-label="Illustration of an online payments cloud connected to phone, tablet, desktop and laptop devices"></div>
</section>

<section class="solutions abs">
  <h2 class="section-title abs" style="top:56px">Our Payment Solutions</h2>
  <div class="solution abs" style="left:110px;top:130px">
    <div class="badge"><svg width="64" height="44" viewBox="0 0 64 44" fill="none" stroke="#fff" stroke-width="2.5"><rect x="10" y="3" width="44" height="30" rx="2"/><path d="M2 37h60l-3 5H5z"/></svg></div>
    <h3>Online</h3>
    <p>Sed ut perspiciatis unde omnis iste natus error sit voluptatem accusantium doloremque</p>
    <span class="btn-outline">Learn More</span>
  </div>
  <div class="solution abs" style="left:448px;top:130px">
    <div class="badge"><svg width="34" height="60" viewBox="0 0 34 60" fill="none" stroke="#fff" stroke-width="2.5"><rect x="3" y="2" width="28" height="56" rx="4"/><line x1="3" y1="10" x2="31" y2="10"/><line x1="3" y1="48" x2="31" y2="48"/><circle cx="17" cy="53" r="1.5" fill="#fff"/></svg></div>
    <h3>Mobile</h3>
    <p>Sed ut perspiciatis unde omnis iste natus error sit voluptatem accusantium doloremque</p>
    <span class="btn-outline">Learn More</span>
  </div>
  <div class="solution abs" style="left:780px;top:130px">
    <div class="badge"><svg width="70" height="56" viewBox="0 0 70 56" fill="none" stroke="#fff" stroke-width="2.5"><path d="M8 4c-4 3-5 8-2 13l6 9c3 4 6 5 9 3l-5-8-4 1-3-6 3-3z" fill="#fff"/><rect x="22" y="20" width="44" height="32" rx="2"/><path d="M22 20l22 18 22-18"/></svg></div>
    <h3>Phone &amp; Email</h3>
    <p>Sed ut perspiciatis unde omnis iste natus error sit voluptatem accusantium doloremque</p>
    <span class="btn-outline">Learn More</span>
  </div>
</section>

<section class="about abs">
  <h2 class="section-title abs" style="top:48px">About Us</h2>
  <p class="body-copy abs" style="top:124px">Donec quam felis, ultricies nec, pellentesque eu, pretium quis, sem. Nulla consequat massa quis enim. Donec pede justo, fringilla vel, aliquet nec, vulputate eget, arcu. In enim justo, rhoncus ut, imperdiet a, venenatis vitae, justo. Nullam dictum felis eu pede mollis pretium. Integer tincidunt. Cras dapibus. Vivamus elementum semper nisi. Aenean vulputate eleifend tellus. Aenean leo ligula, porttitor eu, consequat vitae, eleifend ac, enim. Aliquam lorem ante, dapibus in, viverra quis, feugiat a, tellus. Phasellus viverra nulla ut metus varius laoreet. Quisque rutrum. Aenean imperdiet.</p>
  <div class="btn-solid abs">Read More</div>
</section>

<section class="why abs">
  <h2 class="section-title abs" style="top:66px">Why Halvard Remit</h2>
  <p class="body-copy abs" style="top:140px;left:130px;font-size:15px;line-height:26px">Donec quam felis, ultricies nec, pellentesque eu, pretium quis, sem. Nulla consequat massa quis enim. Donec pede justo, fringilla vel, aliquet nec, vulputate eget, arcu. In enim justo, rhoncus ut, imperdiet a, venenatis vitae, justo. Nullam dictum</p>
  <div class="video abs" role="img" aria-label="Video still of hands holding a tablet and a payment card on a desk">
    <svg width="100" height="100" viewBox="0 0 100 100"><circle cx="50" cy="50" r="42" fill="rgba(0,0,0,.35)" stroke="#fff" stroke-width="4"/><path d="M40 30l30 20-30 20z" fill="#fff"/></svg>
  </div>
</section>

<section class="testimonials abs">
  <h2 class="section-title abs" style="top:48px">What Our Customer Says</h2>
  <div class="avatar abs" style="left:92px;top:150px" role="img" aria-label="Portrait of a customer"></div>
  <p class="quote abs" style="left:258px;top:158px">Donec quam felis, ultricies nec, pellentesque eu, pretium quis, sem. Nulla consequat massa quis enim. Donec pede justo, fringilla vel, aliquet nec, vulputate eget, arcu. In enim justo, eet. "<b>Orla Venn</b></p>
  <div class="avatar abs" style="left:658px;top:150px" role="img" aria-label="Portrait of a customer"></div>
  <p class="quote abs" style="left:822px;top:158px">Donec quam felis, ultricies nec, pellentesque eu, pretium quis, sem. Nulla consequat massa quis enim. Donec pede justo, fringilla vel, aliquet nec, vulputate eget, arcu. In enim justo, eet. "<b>Orla Venn</b></p>
  <div class="avatar abs" style="left:92px;top:328px" role="img" aria-label="Portrait of a customer"></div>
  <p class="quote abs" style="left:258px;top:338px">Donec quam felis, ultricies nec, pellentesque eu, pretium quis, sem. Nulla consequat massa quis enim. Donec pede justo, fringilla vel, aliquet nec, vulputate eget, arcu. In enim justo, eet. "<b>Orla Venn</b></p>
  <div class="avatar abs" style="left:658px;top:328px" role="img" aria-label="Portrait of a customer"></div>
  <p class="quote abs" style="left:822px;top:338px">Donec quam felis, ultricies nec, pellentesque eu, pretium quis, sem. Nulla consequat massa quis enim. Donec pede justo, fringilla vel, aliquet nec, vulputate eget, arcu. In enim justo, eet. "<b>Orla Venn</b></p>
</section>

<footer class="site-footer abs">
  <div class="footer-links abs"><span>Home</span><span>About Us</span><span>Why Halvard Remit</span><span>Services</span><span>Blog</span><span>Testimonials</span><span>Our partners</span><span>Contact</span></div>
  <div class="copyright abs">All rights reserved. copyrights @ 2014</div>
  <div class="social abs"><i></i><i></i><i></i><i></i></div>
</footer>

</body>
</html>
```